Investment Management Firm Power point template

Kestrel Holdings is a real estate investment firm focused on buying commercial office and residential property in the UK. We produce powerpoint presentations for our Board of Directors, Investment Committee and also to external investors.

We are looking for a powerpoint design template which we can use for future presentations which provide a professional look and feel.

Our current website: http://www.kestrelholdings-example.co.uk/

Target Market(s)

Institution Investors, Board of Directors, Professionals

Industry/Entity Type

Real Estate

Requirements
Must have
• Leverage off the current logo and colour scheme. However, does not have to purely rely on this colour scheme.
• - Title page
• - Content Page
• - Slide where graphs can be incorporated
• - Slide where photos can be incorporated
• - Slide of UK Map which can show where the property portfolio is currently located
• - Other slides incorporating smart art or other designs that can be used for future presentations
Nice to have
• An example of graphics that we would love to have in the powerpoint pack which we can easily edit has been attached

```html
<!DOCTYPE html>
<html lang="en">
<head>
<meta charset="utf-8">
<title>Kestrel Holdings – Presentation Template</title>
<link href="https://fonts.googleapis.com/css2?family=Titillium+Web:wght@300;400;600&family=Open+Sans:ital,wght@0,400;0,600;1,400&display=swap" rel="stylesheet">
<style>
:root{
  --navy:#1f3b6e;
  --navy-dark:#172e57;
  --orange:#f07f2c;
  --paper:#eef0f3;
  --white:#ffffff;
  --ink:#2b2f38;
  --muted:#9aa1ad;
  --stage:#d9dbe0;
}
*{box-sizing:border-box;margin:0;padding:0}
html,body{width:1200px;height:1128px;overflow:hidden;background:var(--stage)}
body{font-family:"Open Sans",Arial,sans-serif;color:var(--ink)}
.deck{display:grid;grid-template-columns:repeat(3,1fr);grid-template-rows:repeat(5,1fr);gap:6px;padding:8px;width:1200px;height:1128px}
.slide{position:relative;background:var(--paper);overflow:hidden}
.head{position:absolute;left:0;top:0;right:0;height:30px;background:var(--navy)}
.head h2{position:absolute;left:10px;top:5px;font:300 15px/20px "Titillium Web",sans-serif;color:var(--white)}
.brand-box{position:absolute;right:8px;top:6px;height:19px;border:1px solid rgba(255,255,255,.85);display:flex;align-items:center;gap:4px;padding:0 6px;color:var(--white);font:600 8px/1 "Titillium Web",sans-serif}
.brand-box .sq{width:9px;height:9px;border:1px solid var(--white)}
.rule{position:absolute;left:0;right:0;bottom:10px;height:1px;background:var(--navy)}
.url{position:absolute;left:0;bottom:8px;background:var(--navy);color:var(--white);font:4.6px/6px "Open Sans",sans-serif;padding:0 12px 0 5px;clip-path:polygon(0 0,100% 0,88% 100%,0 100%)}
.pg{position:absolute;right:0;bottom:0;width:30px;height:13px;background:var(--orange);color:var(--white);font:5px/13px "Open Sans",sans-serif;text-align:center;clip-path:polygon(25% 0,100% 0,100% 100%,0 100%)}
.photo{position:absolute}
.body-text{font-size:4.6px;line-height:1.35;color:#3a3f49}
.body-text p{margin-bottom:4px}
.brand{font:600 19px/1 "Titillium Web",sans-serif;color:var(--navy);display:flex;align-items:center;gap:6px}
.brand .sq{width:18px;height:18px;background:var(--navy)}
.title-big{font:300 17px/1.1 "Titillium Web",sans-serif;color:var(--navy)}
.sub-orange{font:400 7px/1.2 "Titillium Web",sans-serif;color:var(--orange)}

/* cover 1 */
.cover-a .photo{inset:0;background:linear-gradient(180deg,#e6e7e9 0%,#cfd1d4 55%,#9a9ca0 100%)}
.cover-a .board{position:absolute;left:88px;top:22px;width:214px;height:84px;background:rgba(255,255,255,.92);box-shadow:0 2px 4px rgba(0,0,0,.25);padding:10px 0 0 24px}
.cover-a .board .title-big{margin-top:6px;font-size:15px}
.cover-a .foot{position:absolute;left:0;right:0;bottom:0;height:14px;background:var(--navy);color:var(--white);font:5.5px/14px "Open Sans",sans-serif;text-align:right;padding-right:14px}
.cover-a .foot .stripe{position:absolute;left:238px;top:0;width:36px;height:14px;background:var(--orange);clip-path:polygon(25% 0,70% 0,45% 100%,0 100%)}
.cover-a .foot .stripe2{position:absolute;left:262px;top:0;width:24px;height:14px;background:var(--white);clip-path:polygon(40% 0,70% 0,40% 100%,10% 100%)}

/* cover 2 */
.cover-b{background:var(--paper)}
.cover-b .brand{position:absolute;left:10px;top:22px;font-size:26px}
.cover-b .brand .sq{width:26px;height:26px}
.cover-b .band{position:absolute;left:0;right:0;top:70px;height:112px;background:var(--navy);border-top:2px solid var(--orange)}
.cover-b .band h1{position:absolute;left:10px;top:20px;font:300 21px/1 "Titillium Web",sans-serif;color:var(--white)}
.cover-b .band p{position:absolute;left:11px;top:44px;font:400 9px/1 "Titillium Web",sans-serif;color:var(--white)}
.cover-b .url{bottom:38px;background:#2d4a80}

/* cover 3 */
.cover-c{background:var(--white)}
.cover-c .photo{left:0;right:0;top:0;height:150px;background:linear-gradient(135deg,#2b3f5c 0%,#5e7591 40%,#c8cfd8 70%,#6b7d93 100%)}
.cover-c svg.wave{position:absolute;left:0;top:120px;width:100%;height:40px}
.cover-c .brand{position:absolute;left:8px;top:172px;font-size:16px}
.cover-c .brand .sq{width:15px;height:15px}
.cover-c .divider{position:absolute;left:168px;top:168px;width:1px;height:30px;background:var(--navy)}
.cover-c .tt{position:absolute;left:181px;top:170px}
.cover-c .tt .title-big{font-size:15px}

/* toc */
.toc{position:absolute;left:50px;top:44px;display:grid;grid-template-columns:180px 150px;row-gap:12px}
.toc li{list-style:none;display:flex;align-items:center;gap:9px;font:400 8px/1 "Open Sans",sans-serif;color:#555b66}
.toc .num{width:31px;height:20px;background:var(--navy);color:var(--white);font:400 10px/20px "Titillium Web",sans-serif;text-align:center}

/* mission */
.mission .lead{position:absolute;left:16px;right:16px;top:38px;font:italic 400 6.4px/1.35 "Open Sans",sans-serif;color:var(--navy);text-align:center}
.mission .body-text{position:absolute;left:10px;top:64px;width:206px}
.mission .hl{color:var(--orange)}
.mission .photo{left:218px;top:74px;width:164px;height:114px;background:linear-gradient(160deg,#e8ecf2 0%,#b7c3d4 45%,#4d5a6e 100%)}

/* team */
.team{position:absolute;left:8px;right:8px;top:46px;display:grid;grid-template-columns:repeat(4,1fr);gap:6px;text-align:center}
.team .avatar{width:44px;height:44px;margin:0 auto;background:linear-gradient(180deg,#c9ccd1,#8b9099)}
.team h3{font:300 9px/1 "Titillium Web",sans-serif;color:var(--navy);margin-top:6px}
.team .role{font:400 6px/1 "Titillium Web",sans-serif;color:var(--orange);margin-top:1px}
.team .body-text{margin-top:8px;text-align:center}

/* two column */
.two-col{position:absolute;left:15px;right:15px;top:45px;display:grid;grid-template-columns:1fr 1fr;gap:20px}

/* image */
.image-slide .photo{left:0;right:0;top:30px;height:102px;background:linear-gradient(120deg,#5b4634 0%,#8a6b4f 35%,#c2b5a4 60%,#6d5640 100%)}
.image-slide h3{position:absolute;left:10px;top:137px;font:400 8px/1 "Titillium Web",sans-serif;color:var(--navy)}
.image-slide .body-text{position:absolute;left:10px;right:10px;top:147px}

/* icons */
.icons{position:absolute;left:10px;right:10px;top:44px;display:grid;grid-template-columns:repeat(4,1fr);row-gap:12px;text-align:center}
.icons svg{width:26px;height:26px;display:block;margin:0 auto}
.icons h4{font:600 5.4px/1 "Open Sans",sans-serif;color:var(--navy);margin-top:3px}
.icons p{font-size:4.3px;line-height:1.3;color:var(--muted);margin-top:2px;padding:0 4px}

/* section */
.section .mark{position:absolute;left:18px;top:24px;width:30px;height:30px;background:var(--navy)}
.section .vline{position:absolute;left:56px;top:22px;width:1px;height:34px;background:#b9bec8}
.section h2{position:absolute;left:64px;top:28px;font:300 13px/1 "Titillium Web",sans-serif;color:var(--ink)}
.section .band{position:absolute;left:0;right:0;top:84px;height:54px;background:var(--navy)}
.section .band p{position:absolute;left:82px;top:10px;width:170px;font-size:5px;line-height:1.4;color:#d6dbe6}
.section .go{position:absolute;right:0;top:0;width:54px;height:54px;background:var(--orange)}
.section .go svg{width:54px;height:54px}

/* table */
.table-slide .intro{position:absolute;left:34px;right:28px;top:42px;font-size:5.6px;line-height:1.35;color:#3a3f49}
.table-slide table{position:absolute;left:52px;top:64px;width:285px;border-collapse:collapse;font:400 5px/1 "Open Sans",sans-serif;box-shadow:0 4px 6px rgba(0,0,0,.15)}
.table-slide th{background:var(--navy);color:var(--white);font-weight:400;height:12px;border-right:1px solid #3c5a8d}
.table-slide th:first-child{background:var(--navy)}
.table-slide td{height:14.6px;text-align:center;color:#3a3f49;background:#dfe3ea;border-right:1px solid #f5f6f8;border-bottom:1px solid #f5f6f8}
.table-slide tr:nth-child(even) td{background:#eceff4}
.table-slide td.phase{background:var(--orange)!important;color:var(--white);text-align:left;padding-left:4px;width:40px}
.table-slide .outro{position:absolute;left:38px;right:10px;top:191px;font-size:5.6px;color:#3a3f49}

/* graphs */
.graph .intro{position:absolute;left:30px;right:24px;top:42px;font-size:5.6px;line-height:1.35;color:#3a3f49}
.graph svg{position:absolute;left:20px;top:62px;width:360px;height:120px}
.graph .outro{position:absolute;left:34px;right:10px;top:188px;font-size:5.6px;color:#3a3f49}

/* strategy */
.strategy .photo{left:0;right:0;top:0;height:134px;background:linear-gradient(180deg,#f3f3f2 0%,#dcdcdb 70%,#b9bcc2 100%)}
.strategy .band{position:absolute;left:0;right:0;top:134px;bottom:0;background:var(--navy)}
.feature-row{position:absolute;left:10px;right:10px;top:112px;display:grid;grid-template-columns:repeat(4,1fr);text-align:center}
.feature-row .disc{width:44px;height:44px;border-radius:50%;background:var(--navy);border:3px solid var(--white);margin:0 auto;display:flex;align-items:center;justify-content:center}
.feature-row .disc svg{width:22px;height:22px}
.feature-row h4{font:600 5.6px/1 "Open Sans",sans-serif;color:var(--white);margin-top:6px}
.feature-row p{font-size:4.6px;line-height:1.3;color:#d6dbe6;margin-top:3px;padding:0 10px}

/* contact */
.contact .photo{left:0;right:0;top:30px;height:120px;background:linear-gradient(135deg,#eceae4 0%,#dcdad3 50%,#e8e4d6 100%)}
.contact .band{position:absolute;left:0;right:0;top:150px;bottom:0;background:var(--navy)}
.contact-row{position:absolute;left:6px;right:6px;top:140px;display:grid;grid-template-columns:repeat(4,1fr)}
.contact-row .disc{width:28px;height:28px;border-radius:50%;background:var(--white);border:2px solid var(--navy);margin:0 auto;display:flex;align-items:center;justify-content:center}
.contact-row .disc svg{width:15px;height:15px}
.contact-row p{font:italic 400 5.4px/1.35 "Open Sans",sans-serif;color:var(--white);margin-top:8px;text-align:center}
.contact-row p.left{text-align:left}

/* thanks */
.thanks{background:var(--white)}
.thanks .brand{position:absolute;left:12px;top:18px;font-size:26px}
.thanks .brand .sq{width:28px;height:28px}
.thanks .photo{left:0;right:0;top:70px;height:136px;background:linear-gradient(120deg,#273a5e 0%,#3e5683 40%,#c19a83 60%,#2d4168 100%)}
.thanks .q{position:absolute;left:84px;top:70px;width:178px;height:42px;background:var(--navy);text-align:center;color:var(--white)}
.thanks .q p{font:400 7px/1 "Titillium Web",sans-serif;margin-top:7px}
.thanks .q h2{font:300 18px/1 "Titillium Web",sans-serif;margin-top:2px}
.thanks .foot{position:absolute;left:0;right:0;bottom:0;height:12px;background:var(--white);color:var(--navy);font:5.5px/12px "Open Sans",sans-serif;text-align:right;padding-right:14px}
.thanks .foot .stripe{position:absolute;left:236px;top:0;width:34px;height:12px;background:var(--orange);clip-path:polygon(25% 0,70% 0,45% 100%,0 100%)}
</style>
</head>
<body>
<main class="deck">

  <!-- Cover A -->
  <section class="slide cover-a">
    <div class="photo" role="img" aria-label="Photo of an empty boardroom with leather chairs and a whiteboard"></div>
    <div class="board">
      <div class="brand"><span class="sq"></span>Kestrel Holdings</div>
      <div class="title-big">PRESENTATION TITLE</div>
      <div class="sub-orange">Place Title detail or Description here</div>
    </div>
    <div class="foot"><span class="stripe"></span><span class="stripe2"></span>www.kestrelholdings-example.co.uk</div>
  </section>

  <!-- Cover B -->
  <section class="slide cover-b">
    <div class="brand"><span class="sq"></span>Kestrel Holdings</div>
    <div class="band">
      <h1>PRESENTATION TITLE</h1>
      <p>Place Title detail or Description here</p>
    </div>
    <div class="url">www.kestrelholdings-example.co.uk</div>
  </section>

  <!-- Cover C -->
  <section class="slide cover-c">
    <div class="photo" role="img" aria-label="Photo of a business team in discussion around a table"></div>
    <svg class="wave" viewBox="0 0 390 40" preserveAspectRatio="none">
      <path d="M0 18 C120 40 260 40 390 6 L390 40 L0 40 Z" fill="#ffffff"/>
      <path d="M0 18 C120 40 260 40 390 6" fill="none" stroke="#1f3b6e" stroke-width="2"/>
    </svg>
    <div class="brand"><span class="sq"></span>Kestrel Holdings</div>
    <div class="divider"></div>
    <div class="tt">
      <div class="title-big">PRESENTATION TITLE</div>
      <div class="sub-orange">Place Title detail or Description here</div>
    </div>
  </section>

  <!-- Table of contents -->
  <section class="slide">
    <header class="head"><h2>Table of Contents</h2><div class="brand-box"><span class="sq"></span>Kestrel Holdings</div></header>
    <ul class="toc">
      <li><span class="num">01</span>Introduction</li><li><span class="num">06</span>Portfolio</li>
      <li><span class="num">02</span>About Us</li><li><span class="num">07</span>Pricing</li>
      <li><span class="num">03</span>Our Team</li><li><span class="num">08</span>Financial Data</li>
      <li><span class="num">04</span>Services</li><li><span class="num">09</span>Testimonial</li>
      <li><span class="num">05</span>Solutions</li><li><span class="num">10</span>Contact Us</li>
    </ul>
    <div class="rule"></div><div class="url">www.kestrelholdings-example.co.uk</div><div class="pg">1</div>
  </section>

  <!-- Mission -->
  <section class="slide mission">
    <header class="head"><h2>Our Mission</h2><div class="brand-box"><span class="sq"></span>Kestrel Holdings</div></header>
    <p class="lead">The mission of Kestrel Holdings is to inspire growth companies to capture opportunities in billion dollar markets by inventing the future.</p>
    <div class="body-text">
      <p>We help you achieve the next level of growth, productivity and profitability. Are you anticipating what's going to happen over the next five years? Are you connected to sources of innovation? More importantly, are your competitors?</p>
      <p>Internet of Things, Big Data and Analytics, 3D Printing, and more ... We have the expertise to help Business Leaders discover what's possible, identify exceptional opportunities, and create value in the New IoT Economy.</p>
      <p><span class="hl">Innovation is not mystical.</span> Innovation is methodical and planned. Innovation is necessary. Getting involved in the startup and VC ecosystem is an important step. We can show you how.</p>
      <p><span class="hl">Innovation is created</span> by strategically connecting marketplace trends with specific project planning. Innovation has developed business-driven innovation for anticipating future realities, identifying innovation, and accessing new revenue.</p>
    </div>
    <div class="photo" role="img" aria-label="Photo of business people walking in a bright glass office"></div>
    <div class="rule"></div><div class="url">www.kestrelholdings-example.co.uk</div><div class="pg">1</div>
  </section>

  <!-- Team -->
  <section class="slide">
    <header class="head"><h2>Our Team</h2><div class="brand-box"><span class="sq"></span>Kestrel Holdings</div></header>
    <div class="team">
      <div><div class="avatar" role="img" aria-label="Team member portrait"></div><h3>John Doe</h3><div class="role">Manager</div><div class="body-text"><p>Lorem ipsum dolor sit amet consectetur adipiscing elit. Vestibulum nec eros in dolor posuere interdum.</p><p>Lorem ipsum dolor sit amet consectetur adipiscing elit. Vestibulum nec eros in dolor posuere interdum.</p></div></div>
      <div><div class="avatar" role="img" aria-label="Team member portrait"></div><h3>John Doe</h3><div class="role">Manager</div><div class="body-text"><p>Lorem ipsum dolor sit amet consectetur adipiscing elit. Vestibulum nec eros in dolor posuere interdum.</p><p>Lorem ipsum dolor sit amet consectetur adipiscing elit. Vestibulum nec eros in dolor posuere interdum.</p></div></div>
      <div><div class="avatar" role="img" aria-label="Team member portrait"></div><h3>John Doe</h3><div class="role">Manager</div><div class="body-text"><p>Lorem ipsum dolor sit amet consectetur adipiscing elit. Vestibulum nec eros in dolor posuere interdum.</p><p>Lorem ipsum dolor sit amet consectetur adipiscing elit. Vestibulum nec eros in dolor posuere interdum.</p></div></div>
      <div><div class="avatar" role="img" aria-label="Team member portrait"></div><h3>John Doe</h3><div class="role">Manager</div><div class="body-text"><p>Lorem ipsum dolor sit amet consectetur adipiscing elit. Vestibulum nec eros in dolor posuere interdum.</p><p>Lorem ipsum dolor sit amet consectetur adipiscing elit. Vestibulum nec eros in dolor posuere interdum.</p></div></div>
    </div>
    <div class="rule"></div><div class="url">www.kestrelholdings-example.co.uk</div><div class="pg">1</div>
  </section>

  <!-- Two column -->
  <section class="slide">
    <header class="head"><h2>Two Column</h2><div class="brand-box"><span class="sq"></span>Kestrel Holdings</div></header>
    <div class="two-col">
      <div class="body-text">
        <p>There are many variations of passages of lorem ipsum available, but the majority have suffered alteration in some form, by injected humour, or randomized words which don't look even slightly believable. If you are going to use a passage of lorem ipsum, you need to be sure there isn't anything embarrassing hidden in the middle of text. All the lorem ipsum generators.</p>
        <p>If you are going to use a passage of Lorem Ipsum, you need to be sure there isn't anything embarrassing hidden in the middle of text. All the Lorem Ipsum generators on the Internet tend to repeat predefined chunks as necessary, making this the first true generator on the Internet.</p>
        <p>It uses a dictionary of over 200 Latin words, combined with a handful of model sentence structures, to generate Lorem Ipsum which looks reasonable. The generated Lorem Ipsum is therefore always free from repetition, injected humour, or non-characteristic words etc.</p>
        <p>There are many variations of passages of lorem ipsum available, but the majority have suffered alteration in some form, by</p>
      </div>
      <div class="body-text">
        <p>There are many variations of passages of lorem ipsum available, but the majority have suffered alteration in some form, by injected humour, or randomized words which don't look even slightly believable. If you are going to use a passage of lorem ipsum, you need to be sure there isn't anything embarrassing hidden in the middle of text. All the lorem ipsum generators.</p>
        <p>If you are going to use a passage of Lorem Ipsum, you need to be sure there isn't anything embarrassing hidden in the middle of text. All the Lorem Ipsum generators on the Internet tend to repeat predefined chunks as necessary, making this the first true generator on the Internet.</p>
        <p>It uses a dictionary of over 200 Latin words, combined with a handful of model sentence structures, to generate Lorem Ipsum which looks reasonable. The generated Lorem Ipsum is therefore always free from repetition, injected humour, or non-characteristic words etc.</p>
        <p>There are many variations of passages of lorem ipsum available, but the majority have suffered alteration in some form, by</p>
      </div>
    </div>
    <div class="rule"></div><div class="url">www.kestrelholdings-example.co.uk</div><div class="pg">1</div>
  </section>

  <!-- Image -->
  <section class="slide image-slide">
    <header class="head"><h2>Image</h2><div class="brand-box"><span class="sq"></span>Kestrel Holdings</div></header>
    <div class="photo" role="img" aria-label="Photo of hands writing in a notebook on a wooden desk beside a tablet and a glass"></div>
    <h3>Heading</h3>
    <div class="body-text">
      <p>There are many variations of passages of lorem ipsum available, but the majority have suffered alteration in some form, by injected humour, or randomized words which don't look even slightly believable. If you are going to use a passage of lorem ipsum, you need to be sure there isn't anything embarrassing hidden in the middle of text. All the lorem ipsum generators.</p>
      <p>If you are going to use a passage of Lorem Ipsum, you need to be sure there isn't anything embarrassing hidden in the middle of text. All the Lorem Ipsum generators on the Internet tend to repeat predefined chunks as necessary, making this the first true generator on the Internet. It uses a dictionary of over 200 Latin words, combined with a handful of model sentence structures.</p>
    </div>
    <div class="rule"></div><div class="url">www.kestrelholdings-example.co.uk</div><div class="pg">1</div>
  </section>

  <!-- Icons -->
  <section class="slide">
    <header class="head"><h2>Icons</h2><div class="brand-box"><span class="sq"></span>Kestrel Holdings</div></header>
    <div class="icons">
      <div><svg viewBox="0 0 26 26" fill="none" stroke="#1f3b6e" stroke-width="1.6"><rect x="4" y="3" width="9" height="16" rx="1"/><rect x="12" y="8" width="10" height="15" rx="1"/></svg><h4>Relationship</h4><p>Nullam eu tempor purus. Nunc a leo magna, consequat risus. Nullam eu.</p></div>
      <div><svg viewBox="0 0 26 26" fill="#1f3b6e"><rect x="11" y="2" width="12" height="10"/><rect x="7" y="7" width="12" height="10" stroke="#eef0f3"/><rect x="3" y="13" width="12" height="10" stroke="#eef0f3"/></svg><h4>Double Data</h4><p>Nullam eu tempor purus. Nunc a leo magna, consequat risus. Nullam eu.</p></div>
      <div><svg viewBox="0 0 26 26" fill="none" stroke="#1f3b6e" stroke-width="2"><circle cx="13" cy="14" r="9"/><path d="M13 9v5l3 3M5 5l3-2M21 5l-3-2"/></svg><h4>Time Up</h4><p>Nullam eu tempor purus. Nunc a leo magna, consequat risus. Nullam eu.</p></div>
      <div><svg viewBox="0 0 26 26" fill="#1f3b6e"><path d="M16 2 6 15h6l-3 9 11-14h-6z"/></svg><h4>Fast Response</h4><p>Nullam eu tempor purus. Nunc a leo magna, consequat risus. Nullam eu.</p></div>
      <div><svg viewBox="0 0 26 26" fill="none" stroke="#1f3b6e" stroke-width="2.4" stroke-linecap="round"><path d="M5 21 19 7M7 5l14 14"/><circle cx="20" cy="6" r="3"/></svg><h4>Responsive</h4><p>Nullam eu tempor purus. Nunc a leo magna, consequat risus. Nullam eu.</p></div>
      <div><svg viewBox="0 0 26 26" fill="none" stroke="#1f3b6e" stroke-width="1.8"><path d="M11 2v10M15 2v10"/><circle cx="13" cy="18" r="5"/></svg><h4>Award</h4><p>Nullam eu tempor purus. Nunc a leo magna, consequat risus. Nullam eu.</p></div>
      <div><svg viewBox="0 0 26 26" fill="none" stroke="#1f3b6e" stroke-width="1.8"><rect x="6" y="3" width="14" height="20" rx="2"/><path d="M12 20h2"/></svg><h4>Digitalization</h4><p>Nullam eu tempor purus. Nunc a leo magna, consequat risus. Nullam eu.</p></div>
      <div><svg viewBox="0 0 26 26" fill="#1f3b6e"><rect x="12" y="3" width="2" height="20"/><path d="M4 7h14l3 2.5-3 2.5H4zM21 13H8l-3 2.5 3 2.5h13z"/></svg><h4>Mapping</h4><p>Nullam eu tempor purus. Nunc a leo magna, consequat risus. Nullam eu.</p></div>
    </div>
    <div class="rule"></div><div class="url">www.kestrelholdings-example.co.uk</div><div class="pg">1</div>
  </section>

  <!-- Section divider -->
  <section class="slide section">
    <div class="mark"></div>
    <div class="vline"></div>
    <h2>Section Divider</h2>
    <div class="band">
      <p>Lorem ipsum dolor sit amet, consectetur adipiscing elit. Vestibulum nec eros in dolor posuere interdum. Ut elementum, justo vel pretium condimentum, ante metus sodales nisi, eu aliquet</p>
      <div class="go"><svg viewBox="0 0 54 54" fill="none" stroke="#fff" stroke-width="1.6"><circle cx="27" cy="27" r="15"/><path d="M19 27h15M29 21l6 6-6 6"/></svg></div>
    </div>
  </section>

  <!-- Table -->
  <section class="slide table-slide">
    <header class="head"><h2>Table</h2><div class="brand-box"><span class="sq"></span>Kestrel Holdings</div></header>
    <p class="intro">Lorem ipsum dolor sit amet, consectetur adipiscing elit. Vestibulum nec eros in dolor posuere interdum. Ut elementum, justo vel pretium condimentum,</p>
    <table>
      <tr><th></th><th>JAN</th><th>FEB</th><th>MAR</th><th>APR</th><th>MAY</th><th>JUN</th></tr>
      <tr><td class="phase">Phase1</td><td>XX</td><td>XX</td><td>XX</td><td>XX</td><td>XX</td><td>XX</td></tr>
      <tr><td class="phase">Phase1</td><td>XX</td><td>XX</td><td>XX</td><td>XX</td><td>XX</td><td>XX</td></tr>
      <tr><td class="phase">Phase1</td><td>XX</td><td>XX</td><td>XX</td><td>XX</td><td>XX</td><td>XX</td></tr>
      <tr><td class="phase">Phase1</td><td>XX</td><td>XX</td><td>XX</td><td>XX</td><td>XX</td><td>XX</td></tr>
      <tr><td class="phase">Phase1</td><td>XX</td><td>XX</td><td>XX</td><td>XX</td><td>XX</td><td>XX</td></tr>
      <tr><td class="phase">Phase1</td><td>XX</td><td>XX</td><td>XX</td><td>XX</td><td>XX</td><td>XX</td></tr>
      <tr><td class="phase">Phase1</td><td>XX</td><td>XX</td><td>XX</td><td>XX</td><td>XX</td><td>XX</td></tr>
    </table>
    <p class="outro">Lorem ipsum dolor sit amet, consectetur adipiscing elit. Vestibulum nec eros in dolor posuere interdum</p>
    <div class="rule"></div><div class="url">www.kestrelholdings-example.co.uk</div><div class="pg">1</div>
  </section>

  <!-- Graphs -->
  <section class="slide graph">
    <header class="head"><h2>Graphs</h2><div class="brand-box"><span class="sq"></span>Kestrel Holdings</div></header>
    <p class="intro">Lorem ipsum dolor sit amet, consectetur adipiscing elit. Vestibulum nec eros in dolor posuere interdum. Ut elementum, justo vel pretium condimentum,</p>
    <svg viewBox="0 0 360 120" font-family="Open Sans, sans-serif">
      <g font-size="5.5" fill="#2b2f38" text-anchor="end">
        <text x="12" y="102">0</text><text x="12" y="87.5">1</text><text x="12" y="73">2</text><text x="12" y="58.5">3</text><text x="12" y="44">4</text><text x="12" y="29.5">5</text><text x="12" y="15">6</text>
      </g>
      <path d="M16 13v87h330" stroke="#2b2f38" stroke-width=".6" fill="none"/>
      <g>
        <rect x="26" y="37.6" width="16" height="62.4" fill="#3d57a8"/><rect x="42" y="65.2" width="16" height="34.8" fill="#f07f2c"/><rect x="58" y="71" width="16" height="29" fill="#1f3b6e"/>
        <rect x="115" y="63.7" width="16" height="36.3" fill="#3d57a8"/><rect x="131" y="36.2" width="16" height="63.8" fill="#f07f2c"/><rect x="147" y="71" width="16" height="29" fill="#1f3b6e"/>
        <rect x="204" y="49.2" width="16" height="50.8" fill="#3d57a8"/><rect x="220" y="73.9" width="16" height="26.1" fill="#f07f2c"/><rect x="236" y="56.5" width="16" height="43.5" fill="#1f3b6e"/>
        <rect x="293" y="34.7" width="16" height="65.3" fill="#3d57a8"/><rect x="309" y="59.4" width="16" height="40.6" fill="#f07f2c"/><rect x="325" y="27.5" width="16" height="72.5" fill="#1f3b6e"/>
      </g>
      <g font-size="5.5" fill="#1f3b6e" font-weight="600" text-anchor="middle">
        <text x="50" y="109">Category 1</text><text x="139" y="109">Category 2</text><text x="228" y="109">Category 3</text><text x="317" y="109">Category 4</text>
      </g>
      <path d="M207 17h42v20h-17l-4 4-4-4h-17z" fill="#1f3b6e"/>
      <text x="228" y="31" font-size="10" fill="#fff" text-anchor="middle">87%</text>
    </svg>
    <p class="outro">Lorem ipsum dolor sit amet, consectetur adipiscing elit. Vestibulum nec eros in dolor posuere interdum</p>
    <div class="rule"></div><div class="url">www.kestrelholdings-example.co.uk</div><div class="pg">1</div>
  </section>

  <!-- Strategy features -->
  <section class="slide strategy">
    <div class="photo" role="img" aria-label="Photo of a businessman sketching a strategy diagram on a wall"></div>
    <div class="band"></div>
    <div class="feature-row">
      <div><div class="disc"><svg viewBox="0 0 22 22" fill="none" stroke="#fff" stroke-width="1.8"><circle cx="13" cy="9" r="5"/><path d="M9 13 4 18"/></svg></div><h4>Spying</h4><p>Nullam eu tempor purus. Nunc a leo magna, sit amet consequat risus. Nullam eu tempor purus.</p></div>
      <div><div class="disc"><svg viewBox="0 0 22 22" fill="none" stroke="#fff" stroke-width="1.6"><rect x="3" y="7" width="14" height="8"/><path d="M17 10v2h2"/><rect x="5" y="9" width="6" height="4" fill="#fff"/></svg></div><h4>More Power</h4><p>Nullam eu tempor purus. Nunc a leo magna, sit amet consequat risus. Nullam eu tempor purus.</p></div>
      <div><div class="disc"><svg viewBox="0 0 22 22" fill="none" stroke="#fff" stroke-width="1.6"><circle cx="11" cy="11" r="8"/><path d="M11 11 15 7"/></svg></div><h4>Quick</h4><p>Nullam eu tempor purus. Nunc a leo magna, sit amet consequat risus. Nullam eu tempor purus.</p></div>
      <div><div class="disc"><svg viewBox="0 0 22 22" fill="#fff"><path d="M11 3 16 17H6z"/><rect x="4" y="17" width="14" height="2"/></svg></div><h4>Warning</h4><p>Nullam eu tempor purus. Nunc a leo magna, sit amet consequat risus. Nullam eu tempor purus.</p></div>
    </div>
  </section>

  <!-- Contact -->
  <section class="slide contact">
    <header class="head"><h2>Contact Us</h2><div class="brand-box"><span class="sq"></span>Kestrel Holdings</div></header>
    <div class="photo" role="img" aria-label="Street map showing the office location"></div>
    <div class="band"></div>
    <div class="contact-row">
      <div><div class="disc"><svg viewBox="0 0 16 16" fill="#1f3b6e"><path d="M8 1a5 5 0 0 0-5 5c0 4 5 9 5 9s5-5 5-9a5 5 0 0 0-5-5zm0 7a2 2 0 1 1 0-4 2 2 0 0 1 0 4z"/></svg></div><p class="left">12 Fenwick Row,<br>London W4 2XR</p></div>
      <div><div class="disc"><svg viewBox="0 0 16 16" fill="#1f3b6e"><path d="M4 2l3 3-2 2c1 2 2 3 4 4l2-2 3 3-2 2C7 14 2 9 2 4z"/></svg></div><p>+44 (0) 20 7946 0321</p></div>
      <div><div class="disc"><svg viewBox="0 0 16 16" fill="none" stroke="#1f3b6e" stroke-width="1.4"><rect x="2" y="4" width="12" height="8"/><path d="M2 4l6 5 6-5"/></svg></div><p>info@kestrelholdings-example.co.uk</p></div>
      <div><div class="disc"><svg viewBox="0 0 16 16" fill="none" stroke="#1f3b6e" stroke-width="1.2"><circle cx="8" cy="8" r="6"/><ellipse cx="8" cy="8" rx="2.5" ry="6"/><path d="M2 8h12"/></svg></div><p>www.kestrelholdings-example.co.uk</p></div>
    </div>
  </section>

  <!-- Thank you -->
  <section class="slide thanks">
    <div class="brand"><span class="sq"></span>Kestrel Holdings</div>
    <div class="photo" role="img" aria-label="Photo of two business people shaking hands"></div>
    <div class="q"><p>Thank You for Listening!</p><h2>QUESTIONS?</h2></div>
    <div class="foot"><span class="stripe"></span>www.kestrelholdings-example.co.uk</div>
  </section>

</main>
</body>
</html>
```